Web design for online activity booking website

Our activity booking website uTrundle.net is looking outdated and needing a loving revamp on its design and STRUCTURE. it was initially created as a destination guide before we modified the homepage slightly to sell activities. So please DON'T RELY on the current website for your design. Now, the focus is ACTIVITY, while guide/ info should come only as secondary.

In other words, we will be doing something very similar to Plomaro.com (a bit crowded for our liking) and FindMyTrailpal.com. If you could capture the best essences of both, that would be awesome! Besides, we also like nestlo.com's simplicity.

SIMPLE, CLEAN, BRIGHT, USER and MOBILE FRIENDLY please :)

We have a new logo created and some wireframes (a few more in progress) so you know the basic components required in each page. These are just rough ideas so please ignore the ratio/size, colours etc and if you have a better way of arranging or simplifying things, please do so :)

Help us make it a website that everyone would love!

Thank you in advance for your time and artistry.

Target Market(s)

Internet savvy travellers between 18-65

Industry/Entity Type

Tourism

Number of Pages Required

5+ page

Requirements
Must have
• SIMPLE, CLEAN feel, USER and MOBILE FRIENDLY please :)
• See attachments for rough structure. Will also need standard pages such as:
• - About Us
• - Contact Us
• - Wishlist etc
• Message from our developer "designer to keep layers in PSD format accurately so html/css code does not need to lead a mess in photoshop"
Nice to have
• UPDATE: We are so thrilled to receive so many web designs but on the other hand, the submissions are getting too generic and everyone's designs is almost looking identical (many look like they are “borrowed” from existing popular websites). This is making the selection and decision process very difficult.
• So instead of sending us more of the very similar homepage design with minor tweaks (which we can do during handover section anyway), please send us a design of more specific page of our website. Please refer job brief, file no. 5 - Product detail page.
• This will give us better idea of your skills and choose the best as winner to work on the rest of our web pages.
Should not have
• No dark background please

```html
<!DOCTYPE html>
<html lang="en">
<head>
<meta charset="utf-8">
<title>uTrundle.net – Book Activities</title>
<link href="https://fonts.googleapis.com/css2?family=Open+Sans:wght@400;600;700&family=Raleway:wght@400;500;600;700&display=swap" rel="stylesheet">
<style>
:root{
  --pink:#f0427a;
  --ink:#3b3b3b;
  --muted:#6f6f6f;
  --white:#ffffff;
  --band:#efefef;
  --footer:#4b4b4b;
  --footer-text:#d8d8d8;
  --shade:linear-gradient(180deg,rgba(0,0,0,0) 45%,rgba(0,0,0,.28) 100%);
}
*{box-sizing:border-box;margin:0;padding:0}
html,body{width:1200px;height:3789px;overflow:hidden}
body{position:relative;background:var(--white);font-family:"Open Sans",Arial,sans-serif;color:var(--ink)}

/* Hero */
.hero{position:absolute;left:0;top:0;width:1200px;height:495px;
  background:
    radial-gradient(ellipse 170px 260px at 330px 190px,rgba(200,50,45,.55),rgba(200,50,45,0) 70%),
    radial-gradient(ellipse 700px 160px at 600px 470px,rgba(70,95,55,.75),rgba(70,95,55,0) 80%),
    linear-gradient(180deg,#7f827f 0%,#a3a6a1 40%,#9aa093 68%,#69715c 100%);
  border-bottom:8px solid var(--pink)}
.hero-shade{position:absolute;inset:0;background:linear-gradient(180deg,rgba(0,0,0,.25) 0%,rgba(0,0,0,0) 25%)}
.brand{position:absolute;left:76px;top:26px;display:flex;align-items:center;gap:8px;color:var(--white);
  font-family:"Raleway",sans-serif;font-weight:700;font-size:34px}
.brand-dot{width:12px;height:12px;border-radius:50%;background:var(--pink)}
.brand-tag{position:absolute;left:80px;top:68px;color:var(--white);font-size:7px;letter-spacing:1px;opacity:.85}
.topnav{position:absolute;right:78px;top:40px;display:flex;align-items:center;gap:24px;color:var(--white);font-size:13px}
.topnav .login{border:1px solid var(--white);border-radius:4px;padding:3px 12px}
.hero-title{position:absolute;left:0;width:1200px;top:192px;text-align:center;color:var(--white);
  font-family:"Raleway",sans-serif;font-weight:500;font-size:36px;text-shadow:0 1px 3px rgba(0,0,0,.3)}
.hero-sub{position:absolute;left:0;width:1200px;top:240px;text-align:center;color:var(--white);font-size:17px}
.search{position:absolute;top:364px;height:42px;background:var(--white);border-radius:2px;
  display:flex;align-items:center;justify-content:space-between;padding:0 10px 0 14px;font-size:15px;color:#555}
.search .chev{width:22px;height:22px}
.go{position:absolute;left:798px;top:364px;width:136px;height:42px;background:var(--pink);color:var(--white);
  font-weight:700;font-size:15px;display:flex;align-items:center;justify-content:center;border-radius:2px}

.sec-title{position:absolute;left:0;width:1200px;text-align:center;font-family:"Raleway",sans-serif;
  font-weight:500;font-size:31px;color:var(--ink)}
.sec-rule{position:absolute;left:575px;width:50px;height:3px;background:var(--pink)}

.tile{position:absolute;height:177px;display:flex;align-items:center;justify-content:center;
  color:var(--white);font-family:"Raleway",sans-serif;font-weight:700;font-size:20px;
  text-shadow:0 1px 3px rgba(0,0,0,.7)}
.w1{width:242px}.w2{width:494px}

.more-btn{position:absolute;left:469px;width:258px;height:33px;border:1px solid var(--pink);border-radius:3px;
  color:var(--pink);font-size:11px;font-weight:700;display:flex;align-items:center;justify-content:center}

.video{position:absolute;left:0;top:2065px;width:1200px;height:510px;
  background:
    linear-gradient(180deg,rgba(0,0,0,.1) 0%,rgba(0,0,0,.3) 100%),
    radial-gradient(ellipse 260px 200px at 150px 420px,rgba(150,60,130,.55),rgba(150,60,130,0) 75%),
    radial-gradient(ellipse 300px 220px at 560px 430px,rgba(235,215,205,.6),rgba(235,215,205,0) 75%),
    radial-gradient(ellipse 340px 260px at 1080px 180px,rgba(70,110,60,.7),rgba(70,110,60,0) 75%),
    linear-gradient(100deg,#d6d2c8 0%,#b9a896 35%,#97806c 60%,#7d8a6a 100%)}
.video-title{position:absolute;left:296px;top:2150px;color:var(--white);font-family:"Raleway",sans-serif;
  font-weight:700;font-size:40px;text-shadow:0 2px 4px rgba(0,0,0,.35)}
.video-sub{position:absolute;left:300px;top:2212px;color:var(--white);font-size:15px}
.play{position:absolute;left:548px;top:2285px;width:100px;height:100px}
.video-more{position:absolute;left:571px;top:2441px;width:78px;height:26px;background:var(--pink);color:var(--white);
  font-size:11px;font-weight:700;display:flex;align-items:center;justify-content:center;border-radius:2px}

.welcome-photo{position:absolute;left:76px;top:2714px;width:510px;height:349px;
  background:
    radial-gradient(ellipse 300px 70px at 260px 270px,rgba(220,110,80,.35),rgba(220,110,80,0) 80%),
    linear-gradient(180deg,#6fb3e4 0%,#a9d6f1 26%,#2b86bd 36%,#3aa2cc 46%,#8fd0dc 54%,#e4d5b3 60%,#cdb78f 100%)}
.caption{position:absolute;left:76px;top:3038px;width:510px;height:25px;background:rgba(0,0,0,.55);
  color:var(--white);font-size:11px;font-weight:600;display:flex;align-items:center;justify-content:center}
.welcome-text{position:absolute;left:613px;top:2714px;width:500px;font-size:12.4px;line-height:19px;color:var(--muted)}
.welcome-text p{margin-bottom:14px}

.links-band{position:absolute;left:0;top:3118px;width:1200px;height:323px;background:var(--band)}
.links-title{position:absolute;left:72px;top:3170px;font-family:"Raleway",sans-serif;font-size:26px;font-weight:500;color:var(--ink)}
.links-rule{position:absolute;left:76px;top:3208px;width:40px;height:3px;background:var(--pink)}
.link-col{position:absolute;top:3240px;list-style:none;font-size:12px;color:var(--muted)}
.link-col li{height:25px;line-height:25px}
.link-col li::before{content:"›";color:var(--pink);margin-right:8px}

.newsletter{position:absolute;left:0;top:3441px;width:1200px;height:86px;background:var(--pink)}
.nl-title{position:absolute;left:76px;top:3468px;color:var(--white);font-family:"Raleway",sans-serif;font-size:24px;font-weight:500}
.nl-input{position:absolute;left:371px;top:3470px;width:280px;height:30px;border-bottom:1px solid var(--white);
  color:var(--white);font-size:12px}
.nl-btn{position:absolute;left:663px;top:3470px;width:132px;height:30px;background:#2e2e2e;color:var(--white);
  font-size:12px;font-weight:700;display:flex;align-items:center;justify-content:center}
.social{position:absolute;top:3466px;width:36px;height:36px;border:2px solid var(--white);border-radius:50%;
  background:rgba(255,255,255,.22)}

.footer{position:absolute;left:0;top:3527px;width:1200px;height:262px;background:var(--footer)}
.foot-brand{position:absolute;left:96px;top:3588px;display:flex;align-items:center;gap:10px;color:var(--white);
  font-family:"Raleway",sans-serif;font-weight:700;font-size:50px}
.foot-brand .brand-dot{width:16px;height:16px}
.foot-tag{position:absolute;left:100px;top:3662px;color:var(--white);font-size:8px;letter-spacing:1.5px}
.copy{position:absolute;left:60px;top:3712px;width:310px;text-align:center;color:var(--footer-text);font-size:11.5px;line-height:19px}
.foot-col{position:absolute;top:3574px}
.foot-col h4{color:var(--white);font-size:14px;font-weight:700;margin-bottom:22px}
.foot-col ul{list-style:none;color:var(--footer-text);font-size:11.5px}
.foot-col li{height:25px}
</style>
</head>
<body>

<header class="hero" role="img" aria-label="Cyclist riding a road bike on a misty country road">
  <div class="hero-shade"></div>
  <div class="brand">uTrundle<span class="brand-dot"></span></div>
  <div class="brand-tag">YOUR ADVENTURE STARTS HERE!</div>
  <nav class="topnav">
    <span>Wishlist Cart</span><span>English ▾</span><span>Currency: $ ▾</span><span>Help</span><span class="login">Log In</span>
  </nav>
  <h1 class="hero-title">BOOK ACTIVITIES</h1>
  <p class="hero-sub">Your Adventure Starts Here!</p>
</header>
<div class="search" style="left:265px;width:258px">Choose a destination
  <svg class="chev" viewBox="0 0 22 22"><path d="M5 8l6 6 6-6" fill="none" stroke="#f0427a" stroke-width="2.4"/></svg></div>
<div class="search" style="left:532px;width:253px">Choose an activity
  <svg class="chev" viewBox="0 0 22 22"><path d="M5 8l6 6 6-6" fill="none" stroke="#f0427a" stroke-width="2.4"/></svg></div>
<div class="go">LET'S GO!</div>

<h2 class="sec-title" style="top:537px">Most Popular Destinations</h2>
<div class="sec-rule" style="top:588px"></div>

<div class="tile w1" style="left:101px;top:631px;background:var(--shade),radial-gradient(ellipse at 30% 20%,#b9cbe0,rgba(185,203,224,0) 55%),linear-gradient(170deg,#7f9bbb 0%,#8b7658 45%,#6a5236 75%,#3e3122 100%)" role="img" aria-label="Volcanic landscape of Tenerife">Tenerife</div>
<div class="tile w2" style="left:354px;top:631px;background:var(--shade),radial-gradient(ellipse 300px 60px at 60% 55%,#5b5042,rgba(91,80,66,0) 80%),linear-gradient(180deg,#aebfd0 0%,#9aaabb 30%,#6b6455 52%,#55493a 75%,#3e3528 100%)" role="img" aria-label="Volcanic hills of Lanzarote">Lanzarote</div>
<div class="tile w1" style="left:858px;top:631px;background:var(--shade),radial-gradient(ellipse at 75% 30%,#9a7d5a,rgba(154,125,90,0) 50%),linear-gradient(180deg,#87b6e0 0%,#5d93c7 35%,#2d6294 60%,#264e78 100%)" role="img" aria-label="Coastline of Fuerteventura">Fuerteventura</div>

<div class="tile w1" style="left:101px;top:821px;background:var(--shade),radial-gradient(ellipse at 50% 70%,#8a8470,rgba(138,132,112,0) 55%),linear-gradient(180deg,#a1b3c2 0%,#6e7a6b 40%,#515a48 70%,#343a2c 100%)" role="img" aria-label="Mountain village in Gran Canaria">Gran Canaria</div>
<div class="tile w1" style="left:354px;top:821px;background:var(--shade),radial-gradient(ellipse at 60% 60%,#5fe0e6,rgba(95,224,230,0) 55%),linear-gradient(180deg,#4fc0d6 0%,#1a98bd 45%,#147fa3 70%,#4f6d58 100%)" role="img" aria-label="Turquoise bay of Formentera">Formentera</div>
<div class="tile w1" style="left:606px;top:821px;background:var(--shade),radial-gradient(ellipse at 30% 40%,#e05aa6,rgba(224,90,166,0) 55%),radial-gradient(ellipse at 75% 70%,#e0b070,rgba(224,176,112,0) 50%),linear-gradient(160deg,#b84b8d,#7d5c9d 50%,#4f638a)" role="img" aria-label="Festival crowd in Ibiza">Ibiza</div>
<div class="tile w1" style="left:858px;top:821px;background:var(--shade),radial-gradient(ellipse at 65% 55%,#7a6c55,rgba(122,108,85,0) 50%),linear-gradient(180deg,#a9bccb 0%,#7d8b7a 40%,#55613f 70%,#363f27 100%)" role="img" aria-label="Rock arch on El Hierro">El Hierro</div>

<div class="tile w2" style="left:101px;top:1010px;background:var(--shade),radial-gradient(ellipse 90px 180px at 68% 50%,#dfe8e2,rgba(223,232,226,0) 80%),radial-gradient(ellipse at 85% 30%,#101810,rgba(16,24,16,0) 50%),linear-gradient(150deg,#3c6a35,#5d8a44 45%,#2a4424 80%,#18231a)" role="img" aria-label="Waterfall in green forest on La Palma">La Palma</div>
<div class="tile w2" style="left:606px;top:1010px;background:var(--shade),radial-gradient(ellipse 120px 80px at 78% 55%,#8f8a7a,rgba(143,138,122,0) 80%),linear-gradient(160deg,#2c4828,#62844a 45%,#3f5a34 75%,#27361f)" role="img" aria-label="Stone bridge in lush Madeira greenery">Madeira</div>

<div class="more-btn" style="top:1217px">MORE POPULAR DESTINATIONS</div>

<h2 class="sec-title" style="top:1295px">Most Popular Activities</h2>
<div class="sec-rule" style="top:1346px"></div>

<div class="tile w1" style="left:101px;top:1391px;background:var(--shade),radial-gradient(ellipse at 30% 20%,#dcdcdc,rgba(220,220,220,0) 50%),linear-gradient(160deg,#a4a4a4,#6a6a6a 50%,#2e2e2e)" role="img" aria-label="Cyclist on a mountain bike">Biking</div>
<div class="tile w2" style="left:354px;top:1391px;background:var(--shade),radial-gradient(ellipse 220px 50px at 55% 45%,#f4f6f8,rgba(244,246,248,0) 80%),linear-gradient(180deg,#7aa7d3 0%,#a9c4de 30%,#2f6797 55%,#1e4e7c 100%)" role="img" aria-label="Motor yacht cruising at sea">Boat Trip</div>
<div class="tile w1" style="left:858px;top:1391px;background:var(--shade),radial-gradient(ellipse at 40% 55%,#c9785a,rgba(201,120,90,0) 55%),linear-gradient(180deg,#a8cbe3 0%,#b8846a 50%,#6a5e62 80%,#3e4c5c 100%)" role="img" aria-label="Anglers holding a catch on a fishing boat">Deep Sea Fishing</div>

<div class="tile w1" style="left:101px;top:1580px;background:var(--shade),radial-gradient(ellipse at 40% 15%,#63c3dc,rgba(99,195,220,0) 55%),linear-gradient(180deg,#2892b4,#17698b 60%,#0c4a62)" role="img" aria-label="Scuba divers underwater">Diving</div>
<div class="tile w1" style="left:354px;top:1580px;background:var(--shade),radial-gradient(ellipse at 50% 45%,#50585e,rgba(80,88,94,0) 45%),linear-gradient(180deg,#d6dee4,#98a4ad 55%,#4f5c66)" role="img" aria-label="Helicopter in flight">Helicopter Tours</div>
<div class="tile w1" style="left:606px;top:1580px;background:var(--shade),radial-gradient(ellipse 60px 90px at 50% 75%,#e8f2f8,rgba(232,242,248,0) 80%),linear-gradient(180deg,#95c5e4,#5394c3 55%,#2b6b9b)" role="img" aria-label="Rider on a water jet flyboard">Flyboarding</div>
<div class="tile w1" style="left:858px;top:1580px;background:var(--shade),radial-gradient(ellipse at 50% 65%,#6c6a58,rgba(108,106,88,0) 55%),linear-gradient(180deg,#bcb9a8,#857f68 50%,#4e4a3a)" role="img" aria-label="Quad bikes on a dirt track">Fun Sport</div>

<div class="tile w2" style="left:101px;top:1768px;background:var(--shade),radial-gradient(ellipse 140px 50px at 70% 70%,#c23a34,rgba(194,58,52,0) 80%),linear-gradient(180deg,#8ab4d6 0%,#9aa4ac 35%,#6e6e6e 60%,#444 100%)" role="img" aria-label="Go-kart racing on a track">Go-karting</div>
<div class="tile w2" style="left:606px;top:1768px;background:var(--shade),radial-gradient(ellipse 180px 50px at 50% 75%,#f2f4f6,rgba(242,244,246,0) 80%),linear-gradient(180deg,#4c81ab,#2b5f88 50%,#5f89ad 80%,#9fb4c6)" role="img" aria-label="Jet skis on the water">Jet Ski</div>

<div class="more-btn" style="top:1977px">MORE POPULAR ACTIVITIES</div>

<section class="video" role="img" aria-label="Group of friends touring a sunny hillside town"></section>
<h2 class="video-title">LOREM IPSUM DOLOR SIT AMET</h2>
<p class="video-sub">Ut enim ad minim veniam, quis nostrud exercitation ullamco laboris nisi ut</p>
<svg class="play" viewBox="0 0 100 100" aria-label="Play video">
  <circle cx="50" cy="50" r="46" fill="none" stroke="#fff" stroke-width="5"/>
  <path d="M40 30 L70 50 L40 70 Z" fill="#fff"/>
</svg>
<div class="video-more">MORE</div>

<h2 class="sec-title" style="top:2596px;font-size:33px">Welcome to uTrundle - The island travel guide!</h2>
<div class="sec-rule" style="top:2650px"></div>
<div class="welcome-photo" role="img" aria-label="Sunny beach with umbrellas and blue sea"></div>
<div class="caption">Playa de las Vistas, Los Cristianos, Tenerife.</div>
<div class="welcome-text">
  <p>After a couple of years of extensive research in which our team of writers, researchers and IT whiz kids have been beavering away incessantly, we are delighted to welcome you to uTrundle, our definitive guide to the Canary Islands and the Madeira Archipelago.</p>
  <p>Whether you're looking for sun and sand, a hedonistic weekend or consider yourself to be something of a culture vulture, our aim is to provide all the information you need on our favourite islands.</p>
  <p>We are also already looking to the future; soon we hope to bring you further guides on islands from across the world, whilst also allowing the opportunity to book your activities on the islands directly through us, here at uTrundle.net. Please watch this space!</p>
  <p>In the meantime, if you feel that we've missed something or that the site could be improved, please don't hesitate to get in touch.</p>
</div>

<section class="links-band"></section>
<h3 class="links-title">Optional: links</h3>
<div class="links-rule"></div>
<ul class="link-col" style="left:76px">
  <li>Top things to do in Tenerife</li><li>Top things to do in Barcelona</li><li>Top things to do in Paris</li>
  <li>Top things to do in London</li><li>Top things to do in Berlin</li><li>Top things to do in Kuala Lumpur</li>
</ul>
<ul class="link-col" style="left:346px">
  <li>Top things to do in Barcelona</li><li>Top things to do in Barcelona</li><li>Top things to do in Barcelona</li>
  <li>Top things to do in Barcelona</li><li>Top things to do in Barcelona</li><li>Top things to do in Barcelona</li>
</ul>
<ul class="link-col" style="left:613px">
  <li>Top things to do in Barcelona</li><li>Top things to do in Barcelona</li><li>Top things to do in Barcelona</li>
  <li>Top things to do in Barcelona</li><li>Top things to do in Barcelona</li><li>Top things to do in Barcelona</li>
</ul>
<ul class="link-col" style="left:884px">
  <li>Top things to do in Barcelona</li><li>Top things to do in Barcelona</li><li>Top things to do in Barcelona</li>
  <li>Top things to do in Barcelona</li><li>Top things to do in Barcelona</li><li>Top things to do in Barcelona</li>
</ul>

<section class="newsletter"></section>
<h3 class="nl-title">SIGN UP NEWSLETTER!</h3>
<div class="nl-input">Enter Email Address</div>
<div class="nl-btn">SIGN UP NOW</div>
<span class="social" style="left:853px" aria-label="Social link"></span>
<span class="social" style="left:892px" aria-label="Social link"></span>
<span class="social" style="left:931px" aria-label="Social link"></span>
<span class="social" style="left:970px" aria-label="Social link"></span>
<span class="social" style="left:1009px" aria-label="Social link"></span>
<span class="social" style="left:1048px" aria-label="Social link"></span>
<span class="social" style="left:1087px" aria-label="Social link"></span>

<footer class="footer"></footer>
<div class="foot-brand">uTrundle<span class="brand-dot"></span></div>
<div class="foot-tag">YOUR ADVENTURE STARTS HERE!</div>
<div class="copy">Copyright © 2015 uTrundle.<br>Terms of Use | Privacy Policy | Sitemap</div>
<div class="foot-col" style="left:434px"><h4>COMPANY</h4>
  <ul><li>About uTrundle.net</li><li>Corporate Info</li><li>Site map?</li><li>Blog</li><li>Careers</li></ul></div>
<div class="foot-col" style="left:631px"><h4>SUPPORT</h4>
  <ul><li>Contact us</li><li>FAQs</li><li>Legal</li><li>Privacy Policy</li><li>Legal</li></ul></div>
<div class="foot-col" style="left:790px"><h4>PARTNERSHIPS</h4>
  <ul><li>Supplier sign-up</li><li>Affiliate Programs</li></ul></div>
<div class="foot-col" style="left:992px"><h4>LOG-INS</h4>
  <ul><li>Customers</li><li>Suppliers</li><li>Affiliates</li></ul></div>

</body>
</html>
```